IT Networking company requires a Brochure Design

We require a new design for our company brochure. We'd like a single double-sided A4 design where the front page will have company related information and services and the rear to have customer testimonials. Please refer to attached document for info as well as our website www.velnatech.com.au. maintain website colour schema as we are an environmentally friendly organisation

Industry/Entity Type

It Company

```html
<!DOCTYPE html>
<html lang="en">
<head>
<meta charset="utf-8">
<title>Velnatech – Testimonials</title>
<link href="https://fonts.googleapis.com/css2?family=Exo+2:wght@400&family=Playfair+Display:ital,wght@0,700;1,700&display=swap" rel="stylesheet">
<style>
  :root {
    --forest: #3a5a0c;
    --lime: #e3f46e;
    --panel: #f4f7ee;
    --ink: #1f2a12;
    --white: #ffffff;
  }
  * { margin: 0; padding: 0; box-sizing: border-box; }
  html, body { width: 848px; height: 1200px; overflow: hidden; background: var(--white); }
  .brochure { position: relative; width: 848px; height: 1200px; overflow: hidden; background: var(--panel); }
  .backdrop { position: absolute; inset: 0; width: 848px; height: 1200px; }
  .brand { position: absolute; left: 52px; top: 56px; color: var(--white); font-family: "Exo 2", sans-serif; font-weight: 400; }
  .brand-name { font-size: 58px; line-height: 1; letter-spacing: 1px; }
  .brand-tagline { margin-top: 10px; font-size: 18px; line-height: 1; letter-spacing: 1px; }
  .said-badge {
    position: absolute; left: 658px; top: 258px; width: 142px; height: 58px; border-radius: 50%;
    background: var(--forest); color: var(--white); font-family: "Exo 2", sans-serif;
    font-size: 17px; letter-spacing: 2.5px; line-height: 19px; text-align: center; padding-top: 10px;
  }
  .testimonials { position: absolute; left: 40px; width: 770px; font-family: "Playfair Display", serif; color: var(--ink); }
  .quote { font-size: 10.6px; font-weight: 700; line-height: 19.5px; letter-spacing: 0.55px; }
  .attribution { text-align: center; font-style: italic; font-size: 12.5px; font-weight: 700; line-height: 19px; letter-spacing: 1.4px; margin-top: 2px; }
  .t1 { top: 345px; } .t2 { top: 575px; } .t3 { top: 758px; }
  .partners-label {
    position: absolute; left: 66px; top: 988px; width: 90px; text-align: center; color: var(--white);
    font-family: "Exo 2", sans-serif; font-size: 16px; letter-spacing: 3px; line-height: 20px;
  }
</style>
</head>
<body>
<div class="brochure">
  <svg class="backdrop" viewBox="0 0 636 900" preserveAspectRatio="none" aria-hidden="true">
    <defs>
      <radialGradient id="glow-top" cx="0.85" cy="0.1" r="0.8">
        <stop offset="0" stop-color="#ffffff"/>
        <stop offset="0.4" stop-color="#eef98f"/>
        <stop offset="1" stop-color="#d8ec55"/>
      </radialGradient>
      <radialGradient id="glow-soft" cx="0.5" cy="0.5" r="0.5">
        <stop offset="0" stop-color="#ffffff"/>
        <stop offset="0.6" stop-color="#eef99a"/>
        <stop offset="1" stop-color="#e3f46e" stop-opacity="0"/>
      </radialGradient>
      <linearGradient id="scene-fade" x1="0" y1="0" x2="0" y2="1">
        <stop offset="0" stop-color="#f4f7ee" stop-opacity="0"/>
        <stop offset="0.2" stop-color="#edf2e4"/>
        <stop offset="0.8" stop-color="#e8eedd"/>
        <stop offset="1" stop-color="#f4f7ee" stop-opacity="0"/>
      </linearGradient>
    </defs>
    <!-- lime burst behind header -->
    <polygon points="0,150 636,0 636,340 560,300 600,260 520,250 470,290 440,240 300,270 240,245 150,290 90,250 0,300" fill="url(#glow-top)"/>
    <!-- faint technology scene -->
    <rect x="0" y="200" width="636" height="520" fill="url(#scene-fade)" role="img" aria-label="Faded photograph of a keyboard and globe"/>
    <!-- lime glows -->
    <ellipse cx="600" cy="320" rx="90" ry="70" fill="url(#glow-soft)"/>
    <ellipse cx="20" cy="250" rx="60" ry="40" fill="url(#glow-soft)"/>
    <ellipse cx="600" cy="610" rx="80" ry="60" fill="url(#glow-soft)"/>
    <ellipse cx="20" cy="620" rx="60" ry="60" fill="url(#glow-soft)"/>
    <!-- header band -->
    <polygon points="0,0 545,0 515,40 590,62 500,95 560,132 470,140 505,188 420,165 440,218 360,186 330,232 290,186 220,214 190,176 110,196 60,170 0,182" fill="var(--forest)"/>
    <!-- footer lime edge -->
    <polygon points="0,690 50,705 75,670 115,705 165,660 195,700 245,670 275,705 320,685 345,715 395,670 435,705 485,660 525,690 575,650 610,680 636,660 636,900 0,900" fill="var(--lime)"/>
    <!-- footer band -->
    <polygon points="0,722 40,740 62,702 102,736 152,692 182,732 232,702 262,737 302,717 332,747 382,702 422,737 472,692 512,722 562,684 602,712 636,694 636,900 0,900" fill="var(--forest)"/>
    <!-- partner badges -->
    <g fill="var(--white)">
      <ellipse cx="65" cy="797" rx="43" ry="17"/>
      <ellipse cx="68" cy="848" rx="47" ry="25"/>
      <ellipse cx="160" cy="815" rx="47" ry="20"/>
      <ellipse cx="213" cy="770" rx="37" ry="16"/>
      <ellipse cx="292" cy="819" rx="52" ry="20"/>
      <ellipse cx="330" cy="775" rx="37" ry="18"/>
      <ellipse cx="423" cy="780" rx="47" ry="29"/>
      <ellipse cx="403" cy="845" rx="72" ry="30"/>
      <ellipse cx="550" cy="760" rx="55" ry="18"/>
      <ellipse cx="536" cy="833" rx="63" ry="33"/>
    </g>
  </svg>

  <header class="brand">
    <div class="brand-name">Velnatech</div>
    <div class="brand-tagline">networks built to last</div>
  </header>

  <div class="said-badge">They've<br>SAID</div>

  <section class="testimonials t1">
    <p class="quote">"Velnatech has transformed our basic network to a fully switched fast domain network with virtualised servers on a Hyperlane platform. Velnatech has always been understanding and conscious of our business needs as all major upgrades over the last 15 years were implemented during our Christmas Holidays whereby there was never any business downtime.<br>The support team is always instantaneously responsive providing the best possible care for both our systems and people. The strategic team always informs us of better ways to execute IT operations and make us aware of new solutions and developments that may or may not enhance our business."</p>
    <p class="attribution">Ms Dana Whitford,<br>"The Insight Data Group"<br>IT Administrator</p>
  </section>

  <section class="testimonials t2">
    <p class="quote">"Our College thanks to Velnatech, now incorporates a wide array of digital learning resources into its curriculum which results in enhanced student engagement and increased learning outcomes. It has a best practice, stable, and well-supported ICT infrastructure which is capable of delivering such digital learning resources.<br>Velnatech has implemented our fibre-backbone network with managed Layer3 switches, virtual LAN segments logically separating staff from students, and an application layer firewall protecting our perimeter network."</p>
    <p class="attribution">Martin Corvalis,<br>"St Aldous College"<br>College Director</p>
  </section>

  <section class="testimonials t3">
    <p class="quote">"Velnatech has been our IT Integration company since 2002. They manage and oversee our IT procurement, Licensing control and renewals, hardware and software upgrades, network design and implementations both at LAN and WAN levels, firewall setup and configuration and web content application controls.<br>At the present moment they are designing and implementing the fibre connection solution to our second office in mascot incorporating a Disaster Recovery solution by duplicating our HEAD OFFICE by virtualised equipment and software. We thank Velnatech for their corporation, understanding and professionalism over the years."</p>
    <p class="attribution">Peter Andronis,<br>"Kestrel Supply PTY LTD"<br>Financial Controller</p>
  </section>

  <div class="partners-label">Our<br>PARTNERS</div>
</div>
</body>
</html>
```